Simple Technical Chart: Illustrating Progress of Paris Climate Talks

Produce a simple, no frills, 1 page, clean technical bar chart from a detailed pencil sketch that is provided with this brief.

All images, data, and text is provided with this brief, in the form of a detailed pencil sketch of the bar chart.

Chart to be produced in landscape format, printed at 8.5" x 11"

The chart illustrates how the country offers for the upcoming Paris climate agreement add-up.

Countries are currently offering carbon emission reductions that will be the basis for a new international agreement on climate change scheduled for finalization in early December in Paris.

This chart compares the results of two different assessments of how the Paris agreement is shaping up: the Tesk et al. assessment, and the Skyline Partners assessment.

1) The chart should be based on the sketch in the uploaded file labeled: TheWholeComplexStory.

2) In addition, our logo should be added to the chart. The file with that logo is labeled: logohires

3) Finally some extra room should be left at the bottom of the chart of the addition of 1-2 lines of text in the way of a footnote. Those two lines of text will be provided separately. Dummy text can be used in first draft.

The images in the file labeled "ParisProgressDraft" and the file labeled "INDCChartV1" are provided for reference ONLY, to help make the concept clear.

The technical chart to be produced should NOT be based on those images. The technical chart should be even simpler, with LESS graphic style.

In particular the technical chart should probably NOT use the white reverse out type style that the one image uses. Reverse out type can be hard to read.

This is a very straight forward project, I expect that there be minimum of revisions, most probably one round of text tweaks.

I will be available to answer any questions.

--

more detail:

There are two bars in this chart - one bar represents the Tesk et al. assessent, the other bar the results of the Skyline Partners assessment. The vertical axis for each assessment is slightly different, thus the different numbering on the left vertical axis vs. the right vertical axis. [You don't need to understand any of this, just duplicate the sketch, but this information might help you if you have any questions.)

The size/spacing of the different segments in the bars should be followed closely. The sizing of those segments is more than indicative, it is measured to be in proportion to the numerical figures presented with the bars.

Target Market(s)

journalists, policy wonks

Industry/Entity Type

Technical

Font styles to use
Sans Serif

Requirements
Must have
• The very bottom of the chart should read:
• This chart illustrates the emerging picture of INDC contributions by comparing and synthesizing findings from two recent assessments of country offers for the Paris agreement: "How high might yearly outputs of carbon pollutants climb by 2040, and could they still fit within keeping temperature rises under 3˚ C by Tesk, Lyall, and Finch, published May 2015 by the Holloway Research Institute and "Rome Brief: Watch the Horizon" February 2015 published by Skyline Partners.

```html
<!DOCTYPE html>
<html lang="en">
<head>
<meta charset="utf-8">
<title>Paris Progress Towards 2° Pathway</title>
<link rel="stylesheet" href="https://fonts.googleapis.com/css2?family=Roboto:wght@300;400;500;700&display=swap">
<style>
  :root {
    --ink: #1c1c1c;
    --bar-text: #0f1f42;
    --label-blue: #5f93dc;
    --frame-blue: #4b84cc;
    --bar-light: #d3e1f6;
    --bar-pale: #ebf1fa;
    --bar-box: #bcd1f0;
    --bar-mid: #a8c5ee;
    --bar-dark: #86abe3;
    --bar-deep: #6d98da;
    --rule: #bfbfbf;
    --paper: #ffffff;
  }
  * { box-sizing: border-box; margin: 0; padding: 0; }
  html, body { width: 1200px; height: 928px; overflow: hidden; background: var(--paper); }
  body { font-family: "Roboto", Arial, sans-serif; color: var(--ink); position: relative; }
  .abs { position: absolute; }
  .guides { position: absolute; left: 0; top: 0; width: 1200px; height: 928px; }

  .brand { left: 40px; top: 22px; font-size: 52px; font-weight: 500; color: var(--label-blue); letter-spacing: -1px; display: flex; align-items: center; gap: 12px; }
  .brand-dot { width: 16px; height: 16px; border-radius: 50%; background: var(--label-blue); }

  .title { left: 428px; top: 33px; font-size: 34px; font-weight: 300; letter-spacing: 1px; color: #3a3a3a; white-space: nowrap; }
  .title .deg { color: var(--label-blue); }

  .panel-head { top: 106px; height: 30px; border: 1px solid #6f8fc0; font-size: 12px; letter-spacing: 2px; display: flex; align-items: center; justify-content: center; color: #333; }
  .panel-head b { font-weight: 700; }

  .segment { position: absolute; display: flex; align-items: center; justify-content: center; text-align: center; color: var(--bar-text); font-weight: 700; font-size: 13px; line-height: 1.45; padding: 0 14px; }
  .seg-light { background: var(--bar-light); }
  .seg-pale { background: var(--bar-pale); }
  .seg-box { background: var(--bar-box); }
  .seg-mid { background: var(--bar-mid); }
  .seg-dark { background: var(--bar-dark); }
  .seg-deep { background: var(--bar-deep); }

  .value { font-size: 19px; font-weight: 700; white-space: nowrap; }
  .value small { font-size: 11px; font-weight: 700; }
  .value .unit-blue { color: var(--label-blue); }
  .note { font-size: 10.5px; color: #333; }
  .pct { font-size: 19px; font-weight: 700; }
  .caption { font-size: 12px; text-align: center; line-height: 1.35; color: #222; }
  .reductions { left: 458px; top: 256px; font-size: 17px; line-height: 1.4; color: #222; }
  .axis-label { font-size: 20px; font-weight: 400; color: var(--label-blue); white-space: nowrap; }
  .axis-label b { font-weight: 700; }
  .circle-note { left: 530px; top: 662px; width: 84px; height: 84px; border: 1.5px solid #222; border-radius: 50%; display: flex; flex-direction: column; align-items: center; justify-content: center; text-align: center; font-size: 10.5px; line-height: 1.2; }
  .circle-note strong { font-size: 18px; }
  .baseline { left: 225px; top: 788px; font-size: 14.5px; line-height: 1.3; padding-left: 6px; border-left: 3px solid var(--label-blue); }
  .baseline b { font-weight: 700; }
  .source { font-size: 11px; color: var(--label-blue); }
  .footnote { left: 40px; top: 838px; width: 1120px; font-size: 12px; line-height: 1.5; color: #333; }
</style>
</head>
<body>

<svg class="guides" viewBox="0 0 1200 928" aria-hidden="true">
  <path d="M405,18 H1132 V10 L1192,56 L1132,102 V94 H405 Z" fill="none" stroke="var(--frame-blue)" stroke-width="1.5"/>
  <line x1="40" y1="150" x2="771" y2="150" stroke="var(--rule)" stroke-width="1.5"/>
  <line x1="984" y1="267" x2="1150" y2="267" stroke="var(--rule)" stroke-width="1.5"/>
  <line x1="50" y1="162" x2="50" y2="780" stroke="#222" stroke-width="2"/>
  <polygon points="50,144 41,164 59,164" fill="#222"/>
  <line x1="40" y1="780" x2="214" y2="780" stroke="#222" stroke-width="2"/>
  <line x1="1132" y1="279" x2="1132" y2="780" stroke="#222" stroke-width="2"/>
  <polygon points="1132,261 1123,281 1141,281" fill="#222"/>
  <line x1="984" y1="780" x2="1142" y2="780" stroke="#222" stroke-width="2"/>
  <line x1="190" y1="377" x2="214" y2="377" stroke="var(--rule)" stroke-width="1.5"/>
  <line x1="214" y1="377" x2="427" y2="377" stroke="#9fb9e3" stroke-width="1.2" stroke-dasharray="9 6"/>
  <line x1="190" y1="626" x2="214" y2="626" stroke="#222" stroke-width="1.5"/>
  <line x1="427" y1="626" x2="442" y2="626" stroke="#222" stroke-width="1.5"/>
  <line x1="427" y1="524" x2="666" y2="524" stroke="#888" stroke-width="1.5" stroke-dasharray="9 6"/>
  <g stroke="var(--label-blue)" stroke-width="2" fill="var(--label-blue)">
    <line x1="726" y1="267" x2="760" y2="267"/><polygon points="770,267 758,261 758,273" stroke="none"/>
    <line x1="726" y1="524" x2="760" y2="524"/><polygon points="770,524 758,518 758,530" stroke="none"/>
    <line x1="726" y1="648" x2="760" y2="648"/><polygon points="770,648 758,642 758,654" stroke="none"/>
  </g>
  <g fill="none" stroke="#222" stroke-width="1.5">
    <path d="M438,156 q8,0 8,8 v165 q0,8 6,8 q-6,0 -6,8 v165 q0,8 -8,8"/>
    <path d="M211,628 q-8,0 -8,8 v60 q0,8 -7,8 q7,0 7,8 v60 q0,8 8,8"/>
    <path d="M987,526 q8,0 8,8 v45 q0,8 6,8 q-6,0 -6,8 v45 q0,8 -8,8"/>
    <path d="M987,650 q8,0 8,8 v49 q0,8 6,8 q-6,0 -6,8 v49 q0,8 -8,8"/>
  </g>
</svg>

<div class="abs brand"><span>Meridia</span><span class="brand-dot"></span></div>
<h1 class="abs title">PARIS PROGRESS TOWARDS <span class="deg">2°</span> PATHWAY</h1>

<div class="abs panel-head" style="left:169px;width:295px;">2030 MILESTONE ON&nbsp;<b>2°</b>&nbsp;PATHWAY</div>
<div class="abs panel-head" style="left:654px;width:446px;"><b>2030</b>&nbsp;EMISSIONS ON LEAST COST PATHWAY TO&nbsp;<b>2°</b></div>

<div class="segment seg-light" style="left:214px;top:150px;width:213px;height:374px;">(&nbsp;Lower ceiling if negative emissions assumed&nbsp;)</div>
<div class="segment seg-mid" style="left:214px;top:524px;width:213px;height:102px;">INDCs to be submitted</div>
<div class="segment seg-dark" style="left:214px;top:626px;width:213px;height:113px;">INDCs submitted by mid-May 2015<br>+<br>Estimate for China</div>
<div class="segment seg-deep" style="left:214px;top:739px;width:213px;height:41px;">Based on Tesk Analysis</div>

<div class="segment seg-pale" style="left:771px;top:150px;width:213px;height:117px;"></div>
<div class="segment seg-box" style="left:795px;top:171px;width:163px;height:72px;">Negative<br>Emissions<br>Assumed</div>
<div class="segment seg-light" style="left:771px;top:267px;width:213px;height:257px;padding:0 22px;">Reductions to be secured through mitigation partnerships i. e. Financing of additional mitigation by developing countries.</div>
<div class="segment seg-mid" style="left:771px;top:524px;width:213px;height:124px;">Optimistic estimate<br>for INDC's to be tabled<br>after US | EU (+ China)</div>
<div class="segment seg-dark" style="left:771px;top:648px;width:213px;height:91px;">US | China | EU | INDC's<br>+<br>Conservative estimate for remaining INDC's</div>
<div class="segment seg-deep" style="left:771px;top:739px;width:213px;height:41px;">Based on Skyline Partners</div>

<div class="abs value" style="left:100px;top:137px;">36 <small class="unit-blue">Gt CO<sub>2</sub> e</small></div>
<div class="abs value" style="left:100px;top:364px;">47 <small>Gt CO<sub>2</sub> e</small></div>
<div class="abs value" style="left:100px;top:613px;">58 <small>Gt CO<sub>2</sub> e</small></div>
<div class="abs note" style="left:150px;top:690px;text-align:center;line-height:1.4;">9.5<br>Gt CO<sub>2</sub> e</div>
<div class="abs value" style="left:80px;top:754px;">67.5 <small class="unit-blue">Gt CO<sub>2</sub> e</small></div>
<div class="abs source" style="left:52px;top:786px;">(est. from Tesk et al.)</div>

<p class="abs reductions">Reductions to be secured<br><u>after</u> Paris through review<br>and&nbsp; Ratchet Mechanism<br>in<br>2020 - 2025 Period<br><span style="padding-left:78px;">+</span><br>2025 - 2030 Period</p>
<div class="abs" style="left:452px;top:562px;font-size:20px;font-weight:700;">?</div>
<div class="abs pct" style="left:445px;top:614px;">30%</div>
<div class="abs caption" style="left:442px;top:642px;width:90px;text-align:left;">(Assuming <u>NO</u> negative emissions)</div>
<div class="abs circle-note"><strong>46%</strong>(If negative emissions secured post 2030)</div>

<div class="abs value" style="left:676px;top:160px;text-align:right;width:48px;">6</div>
<div class="abs note" style="left:660px;top:186px;width:64px;text-align:right;line-height:1.35;font-weight:700;">Gt CO<sub>2</sub> e<br><span style="font-weight:400;">(est.)</span></div>
<div class="abs pct" style="left:662px;top:255px;">100%</div>
<div class="abs pct" style="left:672px;top:512px;">50%</div>
<div class="abs caption" style="left:618px;top:546px;width:145px;">“STRONG SCENARIO”<br><span style="padding-left:40px;display:inline-block;">(Assuming negative emissions)</span></div>
<div class="abs pct" style="left:672px;top:636px;">26%</div>
<div class="abs caption" style="left:620px;top:668px;width:145px;">“WEAK SCENARIO”<br><span style="padding-left:40px;display:inline-block;">(Assuming negative emissions)</span></div>

<div class="abs value" style="left:1037px;top:255px;">42 <small>Gt CO<sub>2</sub> e</small></div>
<div class="abs value" style="left:1008px;top:512px;">55.5 <small>Gt CO<sub>2</sub> e</small></div>
<div class="abs note" style="left:1007px;top:572px;line-height:1.4;">6.5<br>Gt CO<sub>2</sub> e</div>
<div class="abs value" style="left:1015px;top:636px;">62 <small>&nbsp;Gt CO<sub>2</sub> e</small></div>
<div class="abs note" style="left:1007px;top:700px;line-height:1.4;">7<br>Gt CO<sub>2</sub> e</div>
<div class="abs value" style="left:1010px;top:754px;">69 <small class="unit-blue">Gt CO<sub>2</sub> e</small></div>
<div class="abs source" style="left:986px;top:786px;">(Skyline Partners)</div>

<div class="abs axis-label" style="left:-92px;top:453px;width:250px;text-align:center;transform:rotate(-90deg);">Distance to the <b>2°</b> Pathway</div>
<div class="abs axis-label" style="left:1024px;top:511px;width:270px;text-align:center;transform:rotate(-90deg);">The distance to the <b>2°</b> Pathway</div>

<div class="abs baseline">Business As Usual Projection for Emissions in 2030<br><b>Baseline</b></div>

<p class="abs footnote">This chart illustrates the emerging picture of INDC contributions by comparing and synthesizing findings from two recent assessments of country offers for the Paris agreement: “How high might yearly outputs of carbon pollutants climb by 2040, and could they still fit within keeping temperature rises under 3˚ C” by Tesk, Lyall, and Finch, published May 2015 by the Holloway Research Institute and “Rome Brief: Watch the Horizon” February 2015 published by Skyline Partners.</p>

</body>
</html>
```